Corporate Design für Rechtsanwalt (Arbeitsrecht und Gesellschaftsrecht)
Zielgruppe
Rechtsanwalt (Arbeitsrecht und Gesellschaftsrecht)
Aufgabenstellung
Benötigt wird ein schlichtes und modernes Corporate Design für einen Anwalt, der sich vorwiegend mit Arbeitsrecht (Arbeitnehmer wie Arbeitgeber) und Gesellschaftsrecht befasst. Das Logo soll Professionalität und Seriosität vermitteln. Ein Paragraphenzeichen oder eine Waage sollen bitte nicht enthalten sein, da dies „alle“ Rechtsanwälte haben. Die Rechtsgebiete Arbeitsrecht und Gesellschaftsrecht sollen nicht im Logo enthalten sein.
Folgender Inhalt muss untergebracht werden:
Tobias Renz
Rechtsanwalt
Auf dem Briefkopf müssen Bankverbindung, St.-Nr., USt-ID, Internetadresse und Kontaktdaten (Adresse, Telefon, Fax und Mailadresse) untergebracht werden. Diese Daten müssen selbstständig abänderbar sein.
Notwendig sind: Logo, Briefkopf und Visitenkarte.

```html
<!DOCTYPE html>
<html lang="de">
<head>
<meta charset="utf-8">
<title>Tobias Renz – Corporate Design</title>
<link href="https://fonts.googleapis.com/css2?family=Abel&family=Montserrat:wght@300;400&family=Open+Sans:wght@400;700&display=swap" rel="stylesheet">
<style>
  :root {
    --backdrop: #6b6e70;
    --paper: #ffffff;
    --sheet: #f7f7f7;
    --panel: #f3f3f3;
    --accent: #46528a;
    --ink: #2b2b2d;
    --muted: #8a8a8a;
    --body: #333333;
  }
  * { margin: 0; padding: 0; box-sizing: border-box; }
  html, body { width: 1200px; height: 960px; overflow: hidden; }
  body { background: var(--backdrop); position: relative; font-family: "Montserrat", sans-serif; }

  .letterhead {
    position: absolute; left: 131px; top: 163px; width: 437px; height: 619px;
    background: var(--sheet);
  }
  .letterhead .brand { position: absolute; left: 43px; top: 30px; width: 140px; text-align: center; }
  .brand-mark { display: block; margin: 0 auto 8px; width: 34px; height: 34px; background: var(--ink); }
  .letterhead .brand-name {
    font-family: "Montserrat", sans-serif; font-weight: 300; font-size: 17px; color: var(--ink);
    letter-spacing: -0.3px; white-space: nowrap;
  }
  .letterhead .brand-role {
    font-family: "Montserrat", sans-serif; font-size: 6px; letter-spacing: 3.2px; color: var(--ink); margin-top: 5px;
  }
  .sender {
    position: absolute; left: 259px; top: 50px; font-family: "Abel", sans-serif;
    font-size: 10px; line-height: 11.7px; letter-spacing: 1px; color: var(--muted);
  }
  .rule { position: absolute; height: 3px; background: var(--accent); }
  .rule-top { left: 25px; top: 138px; width: 388px; }
  .rule-bottom { left: 22px; top: 555px; width: 394px; }
  .recipient {
    position: absolute; left: 42px; top: 173px; font-family: "Abel", sans-serif;
    font-size: 11.5px; line-height: 14.7px; color: #444;
  }
  .letter-body {
    position: absolute; left: 13px; top: 238px; width: 380px; height: 286px;
    background: var(--panel); padding: 22px 0 0 26px;
    font-family: "Open Sans", sans-serif; font-size: 6.6px; line-height: 12.8px; color: var(--body);
  }
  .letter-body p { margin-bottom: 12.8px; width: 318px; }
  .letter-body .salutation, .letter-body .closing { font-weight: 700; }
  .letter-body .closing { position: absolute; left: 26px; top: 253px; line-height: 14px; }
  .letter-footer {
    position: absolute; top: 574px; left: 0; width: 100%; font-family: "Abel", sans-serif;
    font-size: 17px; color: #111;
  }
  .letter-footer span { position: absolute; transform: translateX(-50%); white-space: nowrap; }

  .logo-card {
    position: absolute; left: 682px; top: 180px; width: 321px; height: 245px;
    background: var(--paper); text-align: center;
  }
  .logo-card .brand-mark { width: 78px; height: 78px; margin: 36px auto 26px; }
  .logo-card .brand-name { font-weight: 300; font-size: 33px; color: var(--ink); letter-spacing: -0.5px; }
  .logo-card .brand-role { font-size: 11px; letter-spacing: 7.5px; color: var(--ink); margin-top: 12px; padding-left: 7px; }

  .business-card {
    position: absolute; left: 600px; top: 480px; width: 485px; height: 276px; background: var(--paper);
  }
  .business-card .brand-mark { position: absolute; left: 74px; top: 106px; width: 72px; height: 72px; margin: 0; }
  .card-heading { position: absolute; left: 226px; top: 37px; border-left: 2px solid var(--accent); padding-left: 12px; height: 50px; }
  .card-heading .brand-name { font-weight: 300; font-size: 26px; color: var(--ink); letter-spacing: -0.4px; line-height: 28px; }
  .card-heading .brand-role { font-size: 9px; letter-spacing: 5px; color: var(--ink); margin: 8px 0 0 32px; }
  .contact-list { position: absolute; left: 217px; top: 106px; list-style: none; }
  .contact-list li {
    display: flex; align-items: flex-start; font-size: 13.5px; color: var(--ink);
    height: 25px; line-height: 20px;
  }
  .contact-list li.address { margin-top: 21px; line-height: 16px; }
  .contact-list svg { width: 14px; height: 14px; margin: 3px 16px 0 0; flex: none; fill: var(--accent); }
</style>
</head>
<body>

<section class="letterhead">
  <div class="brand">
    <span class="brand-mark"></span>
    <div class="brand-name">TOBIAS RENZ</div>
    <div class="brand-role">RECHTSANWALT</div>
  </div>
  <address class="sender" style="font-style:normal">
    Marktgasse 14<br>67890 Bergfeld<br>Tel. (0621)9876-54<br>info@kanzlei-renz.example<br>www.kanzlei-renz.example
  </address>
  <div class="rule rule-top"></div>
  <div class="recipient">Lena Hofer<br>Lindenweg 8<br>54321 Talheim</div>
  <div class="letter-body">
    <p class="salutation">Lieber Herr Brandt,</p>
    <p>Ein Briefkopf ist die Kopfzeile am oberen Rand eines Briefpapiers. Die Kopfzeile enthält normalerweise einen Namen und eine Adresse, ein Logo oder Firmen-Design und manchmal ein Hintergrundmuster. Der Begriff „Briefkopf“ wird oft im Zusammenhang mit einem Brief verwendet, um die Kopfzeile bzw. den oberen Bereich eines Briefes in Szene zu setzen.</p>
    <p>Viele Unternehmen und Einzelpersonen bevorzugen es, einen Briefkopf anhand einer Vorlage in einem Textverarbeitungsprogramm oder einer Software-Anwendung zu erstellen. Eine solche Vorlage enthält die gleichen Informationen wie vorgedrucktes Briefpapier, es entstehen aber keine zusätzlichen Kosten. Der Briefkopf kann dann je nach Bedarf auf Briefpapier (oder ein leeres Blatt Papier) auf einem Drucker gedruckt oder elektronisch versendet werden.</p>
    <p>Der Begriff „Briefkopf“ wird oft im Zusammenhang mit einem Brief verwendet, um die Kopfzeile bzw. den oberen Bereich eines Briefes in Szene zu setzen.</p>
    <div class="closing">Mit freundlichen Grüßen,<br>Tobias Renz</div>
  </div>
  <div class="rule rule-bottom"></div>
  <div class="letter-footer">
    <span style="left:124px">Bankverbindung</span>
    <span style="left:248px">St-Nr.</span>
    <span style="left:348px">USt-ID</span>
  </div>
</section>

<section class="logo-card">
  <span class="brand-mark"></span>
  <div class="brand-name">TOBIAS RENZ</div>
  <div class="brand-role">RECHTSANWALT</div>
</section>

<section class="business-card">
  <span class="brand-mark"></span>
  <div class="card-heading">
    <div class="brand-name">TOBIAS RENZ</div>
    <div class="brand-role">RECHTSANWALT</div>
  </div>
  <ul class="contact-list">
    <li><svg viewBox="0 0 24 24"><path d="M6.6 10.8c1.4 2.8 3.8 5.1 6.6 6.6l2.2-2.2c.3-.3.7-.4 1-.2 1.1.4 2.3.6 3.6.6.6 0 1 .4 1 1V20c0 .6-.4 1-1 1C10.6 21 3 13.4 3 4c0-.6.4-1 1-1h3.5c.6 0 1 .4 1 1 0 1.3.2 2.5.6 3.6.1.3 0 .7-.2 1z"/></svg>+49-621-987-654</li>
    <li><svg viewBox="0 0 24 24"><path d="M3 6h18v12H3z" opacity="0"/><path d="M3 5h18c.6 0 1 .4 1 1v1l-10 6L2 7V6c0-.6.4-1 1-1zm-1 4.3l10 6 10-6V18c0 .6-.4 1-1 1H3c-.6 0-1-.4-1-1z"/></svg>kontakt@renz-recht.example</li>
    <li><svg viewBox="0 0 24 24" fill="none" stroke="#46528a" stroke-width="1.8" style="fill:none"><circle cx="12" cy="12" r="9.5"/><ellipse cx="12" cy="12" rx="4.2" ry="9.5"/><path d="M2.5 12h19M4 7h16M4 17h16"/></svg>www.renz-recht.example</li>
    <li class="address"><svg viewBox="0 0 24 24"><path d="M12 3l10 9h-3v9h-5v-6h-4v6H5v-9H2z"/></svg><span>45 Ufer St., Neustadt,<br>NS 67890</span></li>
  </ul>
</section>

</body>
</html>
```